Website Design for a chemical distribution company

Designer must provide full implementation/coding depending on the platform chosen by the client we'd prefer wordpress type CMS system.

We need a modern and bold website setup for our chemical distribution company. It will need to be like a web store however, no purchases take place on the website only inquiries. So for example the customer can go to a product and click on a button that brings up an inquiry window, they populate that with their information and it sends me an email with the inquiry.

We need it done 3 times pretty much the same but maybe a different colour scheme for each industry. for example on the welcome screen we want 3 icons /pictures ie: plastic, resin, industrial. When the customer clicks on the industry they need it directs them to the specific area that is perhaps on a subdomain or somewhere on the main domain but with no relation to the other industries I hope this makes sense. The layout would be the same but their should be some difference such as colours etc.

The site needs to have a powerful search engine that is very accurate.

It will have about 40,000 products and needs to be able to upload our products via an excel spreed sheet.

We need it to look graphically amazing and very easy to use for the customer.

It will also need to have a blog section that we can upload blogs to daily with different sub categories for things such as experiments, news etc.

The front page needs to be have a banner/advertisement window that is easy for us to change with new specials/deals that we bring out.

Basically the site needs to be easy to navigate, easy to get to products and inquire and needs to have a wow factor.

We also need a special requess page that gives the customers the facility to request a product that they can't find on our website.

I need to stress the importance of a search engine on the site that can handle searching through all the products.

We will also give you the words and you will need to put those on to the pages.

You will also be required to upload our catalogue via CSV or Excel to the site on final completion.

Please find similar websites below for companies that similar to us:

www.tarvelo.com
www.brenti-koval.com
http://www.northumlab.com.au

Just to clarify only one of the websites will have 40-50k products the other 2 industries will only have about 200-500 products each. Added Sunday, February 14, 2016

Reason: Finalising designs and need more time.

Target Market(s)

Chemicals, Food, Pharmaceuticals, Business to Business

Industry/Entity Type

It Company

Coding

Coded - Design and coding required

Number of Pages Required

5+ page

Font styles to use
Sans Serif

Requirements
Must have
• Powerful search engine
• Great design
• Easy to use CMS
• SEO
• Mobile Device Compatible

```html
<!DOCTYPE html>
<html lang="en">
<head>
<meta charset="utf-8">
<title>Korvanta – Chemical Supplies</title>
<link href="https://fonts.googleapis.com/css2?family=Open+Sans:wght@400;600;700;800&family=Roboto:wght@300;400&display=swap" rel="stylesheet">
<style>
:root{
  --blue:#0a78c4;
  --blue-dark:#0665a8;
  --blue-light:#4fb2e8;
  --ink:#333;
  --muted:#777;
  --line:#e4e4e4;
  --footer:#1d1f22;
  --white:#fff;
}
*{margin:0;padding:0;box-sizing:border-box}
html,body{width:759px;height:1200px;overflow:hidden}
body{font-family:"Open Sans",sans-serif;color:var(--ink);background:var(--white);position:relative}
.abs{position:absolute}

/* top bar */
.topbar{top:0;left:0;width:759px;height:22px;background:var(--blue);color:var(--white);font-size:7.2px}
.topbar span{position:absolute;top:6px;display:flex;align-items:center;gap:4px}
.topbar svg{width:8px;height:8px;fill:var(--white)}

/* header */
.header{top:22px;left:0;width:759px;height:41px;background:var(--white)}
.brand{left:56px;top:10px;display:flex;align-items:center;gap:5px;font-size:15px;font-weight:700;color:var(--blue)}
.brand i{display:block;width:8px;height:8px;border-radius:50%;background:var(--blue)}
.nav{right:89px;top:15px;display:flex;gap:11.5px;font-size:7.3px;color:#555}
.nav .active{color:var(--blue);position:relative}
.nav .active:after{content:"";position:absolute;left:-3px;right:-3px;top:13px;height:1.5px;background:var(--blue)}
.search-btn{left:684px;top:10px;width:19px;height:19px;border-radius:50%;background:var(--blue);display:flex;align-items:center;justify-content:center}

/* hero */
.hero{top:63px;left:0;width:759px;height:322px;background:linear-gradient(180deg,#2f3a40 0%,#3c4648 45%,#1f2524 100%)}
.hero-kicker{left:69px;top:82px;font-family:Roboto,sans-serif;font-weight:300;font-size:25px;color:var(--blue-light);letter-spacing:.2px}
.hero-title{left:69px;top:108px;font-family:Roboto,sans-serif;font-weight:400;font-size:33px;color:var(--white)}
.hero-text{left:70px;top:153px;width:310px;font-size:8px;line-height:14px;color:var(--white)}
.hero-btn{left:69px;top:210px;width:80px;height:28px;background:var(--blue);color:var(--white);font-size:7px;display:flex;align-items:center;justify-content:center}
.slide-arrow{top:145px;width:25px;height:26px;display:flex;align-items:center;justify-content:center}
.slide-arrow.prev{left:0;background:var(--blue)}
.slide-arrow.next{right:0;background:rgba(0,0,0,.35)}

.request{left:459px;top:44px;width:208px;height:226px;background:var(--blue);color:var(--white)}
.request h3{position:absolute;left:13px;top:9px;font-family:Roboto,sans-serif;font-weight:300;font-size:12px;line-height:15px}
.request h3 b{font-weight:400;font-size:14px}
.request .note{position:absolute;right:12px;top:29px;font-size:6px}
.field{position:absolute;left:12px;width:182px;height:22.5px;background:var(--white);border-radius:1px;color:#888;font-size:6.8px;padding:7px 7px}
.field.text{height:70px}
.submit{position:absolute;left:65px;top:212px;width:66px;height:23px;background:#2b2b2b;color:var(--white);font-size:7.4px;display:flex;align-items:center;justify-content:center}

/* section titles */
.section-title{left:0;width:759px;text-align:center;font-size:15px;font-weight:600;color:#333}
.section-title em{font-style:normal;color:var(--blue)}

/* categories */
.cat{width:180px;text-align:center}
.cat svg{display:block;margin:0 auto}
.cat h4{margin-top:12px;font-weight:400;font-size:10px;color:#444}
.cat .rule{width:18px;height:1.3px;background:var(--blue);margin:7px auto 8px}
.cat p{font-size:7px;line-height:12.4px;color:var(--muted)}

/* offer */
.offer-bg{left:0;top:690px;width:759px;height:85px;background:linear-gradient(90deg,#e9eef2,#f4f6f8 60%,#e6ecf0)}
.offer-band{left:0;top:690px}
.offer-text{left:54px;top:703px;color:var(--white)}
.offer-text .big{font-weight:800;font-size:28px;line-height:30px;letter-spacing:.3px}
.offer-text .mid{font-weight:600;font-size:14px;line-height:15px}
.offer-text .small{font-weight:700;font-size:8px;margin-top:2px}
.offer-btn{left:401px;top:716px;width:103px;height:32px;background:var(--blue);padding:4px}
.offer-btn div{width:100%;height:100%;border:1px dashed rgba(255,255,255,.85);color:var(--white);font-family:Roboto,sans-serif;font-size:12.5px;display:flex;align-items:center;justify-content:center}
.jug{left:571px;top:666px;width:115px;height:130px;border-radius:26px 30px 14px 14px;background:linear-gradient(90deg,#1e8fe0,#3aa4ee 50%,#1677c4)}

/* blogs */
.card{top:845px;width:151px;height:154px;border:1px solid var(--line);background:var(--white)}
.card .photo{height:89px;width:100%}
.card .date{position:absolute;left:8px;top:0;width:26px}
.card .date .d{background:var(--blue);color:var(--white);font-size:11px;font-weight:600;height:20px;padding:3px 0 0 3px}
.card .date .d sup{font-size:6px}
.card .date .m{background:var(--white);color:var(--blue);font-size:6px;text-align:center;height:8px;line-height:8px}
.card h5{font-weight:400;font-size:8.6px;color:#555;margin:5px 0 0 14px}
.card p{font-size:7px;line-height:10.2px;color:#8a8a8a;margin:9px 14px 0 14px}
.overlay-icons{position:absolute;left:48px;top:31px;display:flex;gap:7px}
.overlay-icons span{width:23px;height:23px;border-radius:50%;display:flex;align-items:center;justify-content:center}

/* footer */
.footer{top:1031px;left:0;width:759px;height:140px;background:linear-gradient(180deg,#24272b,#141618);color:var(--white)}
.fcol{top:30px}
.fcol h6{font-family:Roboto,sans-serif;font-weight:400;font-size:13.5px;margin-bottom:8px}
.fcol p,.fcol li{font-size:7.3px;line-height:14px;list-style:none}
.fdiv{top:24px;width:1px;height:96px;background:#444}
.contact-row{display:flex;gap:7px;align-items:flex-start;font-size:7.3px;margin-bottom:8px;line-height:9.5px}
.contact-row svg{width:8px;height:8px;fill:var(--white);flex:none;margin-top:1px}
.social{display:flex;align-items:center;gap:8px;font-size:9.2px;margin-bottom:7px}
.social i{display:block;width:23px;height:23px;border-radius:50%}
.copy{top:1171px;left:0;width:759px;height:29px;background:var(--blue);color:var(--white);font-size:7px;display:flex;align-items:center;justify-content:center}
</style>
</head>
<body>

<div class="abs topbar">
  <span style="left:56px"><svg viewBox="0 0 10 10"><path d="M2 0.5l1.8 2-1 1.2c.6 1.3 1.6 2.3 2.8 2.9l1.1-1 2 1.7-1 1.7C5 9 1 5 .5 1.5z"/></svg>Call us at +123 456 7890</span>
  <span style="left:153px"><svg viewBox="0 0 10 10"><path d="M0 2h10v6H0z M0 2l5 3.5L10 2" fill="none" stroke="#fff"/></svg>info@domain.com</span>
  <span style="left:626px"><svg viewBox="0 0 10 10"><path d="M3 1h6v8H3M1 5h5M4.5 3.5L6 5 4.5 6.5" fill="none" stroke="#fff"/></svg>Login</span>
  <span style="left:665px"><svg viewBox="0 0 10 10"><rect x="2" y="4.5" width="6" height="5"/><path d="M3.3 4.5V3a1.7 1.7 0 0 1 3.4 0v1.5" fill="none" stroke="#fff"/></svg>Register</span>
</div>

<header class="abs header">
  <div class="abs brand"><i></i>Korvanta</div>
  <nav class="abs nav">
    <span class="active">Home</span><span>About Us</span><span>Services</span><span>Products</span><span>Contact</span>
  </nav>
  <div class="abs search-btn"><svg width="8" height="8" viewBox="0 0 10 10"><circle cx="4" cy="4" r="3" fill="none" stroke="#fff" stroke-width="1.4"/><path d="M6.2 6.2L9 9" stroke="#fff" stroke-width="1.4"/></svg></div>
</header>

<section class="abs hero" role="img" aria-label="Dusk photograph of an industrial plant with a tall chimney and trees">
  <div class="abs hero-kicker">BEST CHEMICAL</div>
  <div class="abs hero-title">SUPPLIES DIVISION</div>
  <p class="abs hero-text">Lorem Ipsum is simply dummy text of the printing and typesetting industry. Lorem Ipsum has been the industry's standard dummy text ever since the 1500s, when an unknown printer.</p>
  <div class="abs hero-btn">READ MORE</div>
  <div class="abs slide-arrow prev"><svg width="7" height="9" viewBox="0 0 7 9"><path d="M5 1L2 4.5 5 8" fill="none" stroke="#fff" stroke-width="1.5"/></svg></div>
  <div class="abs slide-arrow next"><svg width="7" height="9" viewBox="0 0 7 9"><path d="M2 1l3 3.5L2 8" fill="none" stroke="#fff" stroke-width="1.5"/></svg></div>

  <form class="abs request">
    <h3>Special<br><b>Request Form</b></h3>
    <span class="note">*All Fields Rquired</span>
    <div class="field" style="top:48px">Customer Name :</div>
    <div class="field" style="top:76px">Email Address :</div>
    <div class="field" style="top:104px">Complain Subject :</div>
    <div class="field text" style="top:132px">Text :</div>
    <div class="submit">Submit</div>
  </form>
</section>

<h2 class="abs section-title" style="top:409px">PRODUCT <em>CATEGORIES</em></h2>

<svg width="0" height="0" style="position:absolute">
  <defs>
    <linearGradient id="hexRim" x1="0" y1="0" x2="0" y2="1"><stop offset="0" stop-color="#5cc0ee"/><stop offset="1" stop-color="#0a6fc0"/></linearGradient>
    <linearGradient id="fillPlastic" x1="0" y1="0" x2="0" y2="1"><stop offset="0" stop-color="#eeeeec"/><stop offset="1" stop-color="#9aa0a4"/></linearGradient>
    <linearGradient id="fillResin" x1="0" y1="0" x2="0" y2="1"><stop offset="0" stop-color="#a7a59f"/><stop offset=".55" stop-color="#8a7146"/><stop offset="1" stop-color="#6b6a66"/></linearGradient>
    <linearGradient id="fillIndustrial" x1="0" y1="0" x2="0" y2="1"><stop offset="0" stop-color="#3f7fd6"/><stop offset=".55" stop-color="#8fb6e6"/><stop offset="1" stop-color="#7a6a5a"/></linearGradient>
  </defs>
</svg>

<div class="abs cat" style="left:62px;top:444px">
  <svg width="108" height="124" viewBox="0 0 108 124"><polygon points="54,0 108,31 108,93 54,124 0,93 0,31" fill="url(#hexRim)"/><polygon role="img" aria-label="White plastic canisters on a production line" points="54,9 100,36 100,88 54,115 8,88 8,36" fill="url(#fillPlastic)"/></svg>
  <h4>PLASTIC</h4><div class="rule"></div>
  <p>Lorem Ipsum is simply dummy text of the printing and typesetting industry. Lorem Ipsum has been the industry's standard dummy text.</p>
</div>
<div class="abs cat" style="left:288px;top:444px">
  <svg width="108" height="124" viewBox="0 0 108 124"><polygon points="54,0 108,31 108,93 54,124 0,93 0,31" fill="url(#hexRim)"/><polygon role="img" aria-label="Close-up of an amber resin droplet on tree bark" points="54,9 100,36 100,88 54,115 8,88 8,36" fill="url(#fillResin)"/></svg>
  <h4>RESIN</h4><div class="rule"></div>
  <p>Lorem Ipsum is simply dummy text of the printing and typesetting industry. Lorem Ipsum has been the industry's standard dummy text.</p>
</div>
<div class="abs cat" style="left:509px;top:444px">
  <svg width="108" height="124" viewBox="0 0 108 124"><polygon points="54,0 108,31 108,93 54,124 0,93 0,31" fill="url(#hexRim)"/><polygon role="img" aria-label="Power plant with red and white chimneys under blue sky" points="54,9 100,36 100,88 54,115 8,88 8,36" fill="url(#fillIndustrial)"/></svg>
  <h4>INDUSTRIAL</h4><div class="rule"></div>
  <p>Lorem Ipsum is simply dummy text of the printing and typesetting industry. Lorem Ipsum has been the industry's standard dummy text.</p>
</div>

<div class="abs offer-bg" role="img" aria-label="Faded laboratory scene with glassware"></div>
<svg class="abs offer-band" width="380" height="85" viewBox="0 0 380 85"><polygon points="0,0 373,0 325,85 0,85" fill="var(--blue)"/><polygon points="373,0 380,0 332,85 325,85" fill="#fff" opacity=".7"/></svg>
<div class="abs offer-text">
  <div class="big">SPECIAL OFEER</div>
  <div class="mid">LIMITED TIME ONLY</div>
  <div class="small">GET OFFER NOW</div>
</div>
<div class="abs offer-btn"><div>VIEW OFFER</div></div>
<div class="abs jug" role="img" aria-label="Blue plastic jerry can product shot"></div>

<h2 class="abs section-title" style="top:809px">LATEST <em>BLOGS</em></h2>

<article class="abs card" style="left:59px">
  <div class="photo" role="img" aria-label="Refinery towers in a green landscape" style="background:linear-gradient(180deg,#b9c4cc,#7d7a6e 60%,#7f8a55)"></div>
  <div class="date"><div class="d">24<sup>th</sup></div><div class="m">FEB</div></div>
  <h5>Blog Post title here</h5>
  <p>Cras dapibus. Vivamus elementum semper nisi enean vulputate tellus. Aenean leo.</p>
</article>
<article class="abs card" style="left:221px">
  <div class="photo" role="img" aria-label="Industrial photograph under a blue hover overlay" style="background:linear-gradient(180deg,#1b82cc,#0f6fb6)"></div>
  <div class="overlay-icons">
    <span style="border:1px solid #fff"><svg width="9" height="9" viewBox="0 0 10 10"><circle cx="4" cy="4" r="3" fill="none" stroke="#fff" stroke-width="1.2"/><path d="M6.2 6.2L9 9" stroke="#fff" stroke-width="1.2"/></svg></span>
    <span style="background:#fff"><svg width="9" height="9" viewBox="0 0 10 10"><circle cx="2" cy="5" r="1.4" fill="none" stroke="#0a78c4"/><circle cx="8" cy="2" r="1.4" fill="none" stroke="#0a78c4"/><circle cx="8" cy="8" r="1.4" fill="none" stroke="#0a78c4"/><path d="M3.2 4.4L6.8 2.6M3.2 5.6l3.6 1.8" stroke="#0a78c4"/></svg></span>
  </div>
  <div class="date"><div class="d">24<sup>th</sup></div><div class="m">FEB</div></div>
  <h5>Blog Post title here</h5>
  <p>Cras dapibus. Vivamus elementum semper nisi enean vulputate tellus. Aenean leo.</p>
</article>
<article class="abs card" style="left:384px">
  <div class="photo" role="img" aria-label="Storage silos and processing plant under a cloudy sky" style="background:linear-gradient(180deg,#7fa7c7,#c9cfd2 55%,#6d6a62)"></div>
  <div class="date"><div class="d">24<sup>th</sup></div><div class="m">FEB</div></div>
  <h5>Blog Post title here</h5>
  <p>Cras dapibus. Vivamus elementum semper nisi enean vulputate tellus. Aenean leo.</p>
</article>
<article class="abs card" style="left:547px">
  <div class="photo" role="img" aria-label="Laboratory glassware with blue liquid and a gloved hand with a pipette" style="background:linear-gradient(135deg,#e6eef4,#7fc0e6 55%,#1d7fc0)"></div>
  <div class="date"><div class="d">24<sup>th</sup></div><div class="m">FEB</div></div>
  <h5>Blog Post title here</h5>
  <p>Cras dapibus. Vivamus elementum semper nisi enean vulputate tellus. Aenean leo.</p>
</article>

<footer class="abs footer">
  <div class="abs fcol" style="left:56px;width:180px">
    <h6>ABOUT</h6>
    <p>Lorem Ipsum is simply dummy text of the printing and typesetting industry. Lorem Ipsum has been the industry's standard dummy text ever since the 1500s</p>
  </div>
  <div class="abs fdiv" style="left:254px"></div>
  <div class="abs fcol" style="left:272px">
    <h6>USEFUL LINKS</h6>
    <ul><li>About Us</li><li>Ordering</li><li>FAQ</li><li>Customer Support</li><li>Special Offers</li></ul>
  </div>
  <div class="abs fdiv" style="left:394px"></div>
  <div class="abs fcol" style="left:418px">
    <h6>CONNECT</h6>
    <div class="contact-row"><svg viewBox="0 0 10 10"><path d="M2 0.5l1.8 2-1 1.2c.6 1.3 1.6 2.3 2.8 2.9l1.1-1 2 1.7-1 1.7C5 9 1 5 .5 1.5z"/></svg>123-456-7890</div>
    <div class="contact-row"><svg viewBox="0 0 10 10"><path d="M0 2h10v6H0z"/><path d="M0 2l5 3.5L10 2" fill="none" stroke="#222"/></svg>info@domain.com</div>
    <div class="contact-row"><svg viewBox="0 0 10 10"><path d="M5 0a3 3 0 0 1 3 3c0 2.3-3 6-3 6S2 5.3 2 3a3 3 0 0 1 3-3z"/></svg><span>Werkhaus<br>Lindenweg 42b<br>10117 Berlin,Germany</span></div>
  </div>
  <div class="abs fdiv" style="left:540px"></div>
  <div class="abs fcol" style="left:559px">
    <h6 style="margin-left:4px">GET IN TOUCH</h6>
    <div class="social"><i style="background:#3b5ba0"></i>Like us on Friendbook</div>
    <div class="social"><i style="background:#27a8e6"></i>Follow us on Chirper</div>
  </div>
</footer>
<div class="abs copy">© 2016 . All rights reserved.</div>

</body>
</html>
```